Music Poster (that is birthday gift.)

We want a rock music poster in the spirit of the old time Copperfield Lantern psychedelic posters that says, "Halvorsen Summer Music Festival" "July 30, 2016." Red Hook, NY. Dwight Tolver is the artist. This is the 4th Annual Event. It is also Neil Halvorsen's 50th birthday.
Happy to answer any questions on email or live. Call Gareth at 212.555.0148

Target Market(s)

Personal gift!

Industry/Entity Type

Festival

Requirements
Must have
• Fabulous Design....

```html
<!DOCTYPE html>
<html lang="en">
<head>
<meta charset="utf-8">
<title>Halvorsen Summer Music Festival — Dwight Tolver</title>
<link rel="stylesheet" href="https://fonts.googleapis.com/css2?family=Macondo+Swash+Caps&family=Bungee&display=swap">
<style>
  :root {
    --frame-dark: #1d2a36;
    --frame-red: #d8371f;
    --field: #2f5470;
    --field-deep: #24445c;
    --title-red: #e0431f;
    --chrome-blue: #1f6fd0;
    --chrome-mid: #8fc2f2;
    --chrome-light: #ffffff;
    --chrome-shadow: #102640;
    --cream: #f6eee0;
    --blush: #f3d6cc;
    --orange: #ee6a1c;
    --yellow: #f2ee32;
    --photo-navy: #1f2454;
    --photo-gold: #e9a93a;
    --photo-rust: #b8482a;
  }
  * { margin: 0; padding: 0; box-sizing: border-box; }
  html, body { width: 900px; height: 1200px; overflow: hidden; background: var(--frame-dark); }
  .poster {
    position: relative;
    width: 900px; height: 1200px;
    background: var(--frame-dark);
    padding: 18px;
  }
  .poster-field {
    position: relative;
    width: 100%; height: 100%;
    border: 5px solid var(--frame-red);
    background: radial-gradient(ellipse at 40% 40%, var(--field) 0%, var(--field) 60%, var(--field-deep) 100%);
    overflow: hidden;
  }
  .artist-photo {
    position: absolute;
    left: 395px; top: 105px;
    width: 470px; height: 1060px;
    background: linear-gradient(165deg, var(--photo-rust) 0%, var(--photo-gold) 20%, var(--photo-navy) 42%, var(--photo-navy) 78%, var(--photo-rust) 100%);
    clip-path: polygon(62% 0, 82% 1%, 94% 10%, 100% 18%, 100% 100%, 8% 100%, 12% 70%, 18% 50%, 30% 36%, 44% 28%, 52% 16%);
  }
  .poster-type {
    position: absolute;
    inset: 0;
    width: 100%; height: 100%;
  }
  .birthday-line {
    font-family: "Macondo Swash Caps", serif;
    fill: var(--title-red);
  }
  .series-title {
    font-family: "Macondo Swash Caps", serif;
    fill: url(#chrome);
    stroke: var(--chrome-shadow);
    stroke-width: 3px;
    paint-order: stroke;
  }
  .headliner {
    font-family: "Bungee", sans-serif;
    fill: url(#cream);
    stroke: var(--orange);
    stroke-width: 4px;
    paint-order: stroke;
  }
  .event-details {
    font-family: "Macondo Swash Caps", serif;
    fill: var(--yellow);
  }
</style>
</head>
<body>
<div class="poster">
  <div class="poster-field">
    <div class="artist-photo" role="img" aria-label="Posterised photograph of the performer holding an acoustic guitar, in navy, gold and rust tones"></div>

    <svg class="poster-type" viewBox="0 0 854 1154" aria-labelledby="poster-heading">
      <defs>
        <linearGradient id="chrome" x1="0" y1="0" x2="0" y2="1">
          <stop offset="0" stop-color="var(--chrome-blue)"/>
          <stop offset="0.35" stop-color="var(--chrome-mid)"/>
          <stop offset="0.55" stop-color="var(--chrome-light)"/>
          <stop offset="1" stop-color="var(--chrome-blue)"/>
        </linearGradient>
        <linearGradient id="cream" x1="0" y1="0" x2="1" y2="0">
          <stop offset="0" stop-color="var(--blush)"/>
          <stop offset="0.5" stop-color="var(--cream)"/>
          <stop offset="1" stop-color="var(--blush)"/>
        </linearGradient>
      </defs>

      <text class="birthday-line" x="32" y="52" font-size="40" textLength="790" lengthAdjust="spacingAndGlyphs">NEIL HALVORSEN'S 50TH BIRTHDAY</text>

      <g id="poster-heading" class="series-title">
        <text x="30" y="214" font-size="128" textLength="610" lengthAdjust="spacingAndGlyphs">HALVORSEN</text>
        <text x="36" y="346" font-size="138" textLength="560" lengthAdjust="spacingAndGlyphs">SUMMER</text>
        <text x="22" y="476" font-size="138" textLength="460" lengthAdjust="spacingAndGlyphs">MUSIC</text>
        <text x="40" y="608" font-size="134" textLength="580" lengthAdjust="spacingAndGlyphs">FESTIVAL</text>
      </g>

      <g class="headliner">
        <text x="36" y="726" font-size="96" textLength="338" lengthAdjust="spacingAndGlyphs">DWIGHT</text>
        <text x="36" y="856" font-size="132" textLength="338" lengthAdjust="spacingAndGlyphs">TOLVER</text>
      </g>

      <g class="event-details" text-anchor="middle">
        <text x="201" y="906" font-size="42" textLength="372" lengthAdjust="spacingAndGlyphs">4TH ANNUAL EVENT</text>
        <text x="201" y="1004" font-size="88" textLength="356" lengthAdjust="spacingAndGlyphs">RED HOOK</text>
        <text x="201" y="1064" font-size="62" textLength="272" lengthAdjust="spacingAndGlyphs">NEW YORK</text>
        <text x="201" y="1126" font-size="62" textLength="352" lengthAdjust="spacingAndGlyphs">JULY 30, 2016</text>
      </g>
    </svg>
  </div>
</div>
</body>
</html>
```